Veridian Token Bourse (front page)

We need a design of a front page for our Veridian Token Bourse website (vtbex.co.uk). Our company is based in the United Kingdom and offers investors from all over the world an opportunity to invest into bitcoin and litecoin.

We have been developing this cutting edge technology for past 2 years based on our in depth knowledge on conventional stock and currency trading technology and methodology. We have run many test against penetration, security and stability and now are ready to deploy.

Recent news about vulnerability of such platforms leave a great deal of unease from retail investors about investing into cryptocurrency. We are set to challenge this attitude. Our background is payments in particular regulated environment in the UK. We are keen to apply our wealth of experience to provide secure and reliable trading platform and advance cryptocurrency as means of legal tender.

The front page should be based on the feel and look of our current technology vtbex.co.uk. Some of you have already been involved in logo design for our company, please see the attached mockups. The page should have this minimalist design, very clean and light.

Seek inspiration form www.coinharbor.net, www.tradelumo.com, vip.quorzen.com and other bitcoin exchanges.

We look forward to receiving your ideas.

You can also refer to our social pages:
https://www.facebook.com/vtbex.co.uk
https://twitter.com/vtbex_uk

We would like you to focus your efforts at designing the page in such a way so that it is very easy for visitor be open an account with the exchange. We must focus at informing the visitor about the bitcoin, how to my buy, how to sell, look at the general overview of the maker and CONVERTING him/her sing up. This is the most important!!

Regards,
Tobin
Updates

Project Deadline Extended
Reason: Dear all, We are very keen on getting this design done right the first time. The key success is conversion of visitors to subscribers and then to traders. It is absolutely essential make the registration process as streamlined as possible! When we are calling them to act by "Change the world one bitcoin at a time" we should give them a opportunity to provide us with relevant account creation details: email, password, confirm password. Please visit remitfold.co.uk for ideas. Secondly, tell them what is a bitcoin, why a bitcoin is a good investment and how to invest. Finally, it is important to inform visitors of "who we are", what sets us apart from other exchanges, tell them about our experience. In our view graphs and live order books are important but they might turn some visitors away especially the ones that are not accustomed to online trading. Think of what would you like to see on the page if you wanted YOURSELF to invest. What would make you to create an account and use it? Think what will work, we are here to revolutionise how people do business.... any wild ideas put them to us. OUR BUDGET JUST GONE UP!!!

Target Market(s)

A combination of professional and consumer bitcoin investors.

Industry/Entity Type

Environment

Requirements
Must have
• News section

```html
<!DOCTYPE html>
<html lang="en">
<head>
<meta charset="utf-8">
<title>Veridian Token Bourse</title>
<link href="https://fonts.googleapis.com/css2?family=Orbitron:wght@400;500&family=Open+Sans:wght@400;600;700&family=Oswald:wght@500;600&family=PT+Sans:wght@400;700&display=swap" rel="stylesheet">
<style>
:root{
  --blue:#1a9ad6;
  --blue-dark:#1582b8;
  --ink:#3a3a3a;
  --muted:#666;
  --panel:#444648;
  --soft:#eeeeee;
  --white:#fff;
}
*{margin:0;padding:0;box-sizing:border-box}
html,body{width:790px;height:1200px;overflow:hidden;background:var(--white)}
body{position:relative;font-family:Arial,Helvetica,sans-serif;color:var(--ink)}
.abs{position:absolute}

/* header */
.brand{left:86px;top:26px;display:flex;align-items:center;gap:8px}
.brand-name{font-family:"PT Sans",sans-serif;font-weight:700;font-size:15px;line-height:18px;color:var(--ink);white-space:nowrap}
.brand-dot{width:9px;height:9px;border-radius:50%;background:var(--blue)}
.account{left:607px;top:20px;display:flex;gap:2px}
.account span{font-size:7px;color:#fff;padding:4px 7px;height:16px;display:block}
.signup{background:var(--blue)}
.login{background:#3d3d3d}
.nav{right:89px;top:45px;display:flex;gap:6px;font-family:Orbitron,sans-serif;font-size:7.5px;letter-spacing:.6px;color:#666}
.nav .active{color:var(--blue)}

/* ticker */
.ticker{left:0;top:68px;width:790px;height:27px;background:var(--blue);display:flex;padding-left:126px}
.tick{width:110px;display:flex;align-items:center;gap:5px;color:#fff;font-size:7px;line-height:8px;border-right:1px solid rgba(255,255,255,.35);padding-left:8px}
.tick:last-child{border:none}
.tick i{width:17px;height:17px;border:1.5px solid #fff;border-radius:50%;display:block}

/* hero */
.hero-photo{left:0;top:95px;width:790px;height:329px;background:linear-gradient(90deg,#5f93b8 0%,#8db6d2 30%,#4a5a6a 55%,#2f3842 75%,#7fa9c7 100%)}
.coin{left:88px;top:182px;width:76px;height:76px;border-radius:50%;border:5px solid #fff;background:#5b9ec8}
.coin::after{content:"";position:absolute;inset:6px;border-radius:50%;background:#fff}
.hero-copy{left:174px;top:178px;color:#fff}
.hero-copy h1{font-family:Orbitron,sans-serif;font-weight:500;font-size:17px;letter-spacing:1.5px}
.hero-copy p{font-family:"PT Sans",sans-serif;font-size:10px;line-height:12px;margin-top:5px;width:220px}
.hero-btns{display:flex;gap:9px;margin-top:8px}
.hero-btns span{background:#fff;color:#333;font-family:"PT Sans",sans-serif;font-weight:700;font-size:10px;padding:2px 8px;height:17px;border-radius:2px}
.signup-panel{left:446px;top:116px;width:256px;height:214px;background:var(--panel);border-radius:3px;padding:24px 16px 0 16px;color:#fff;opacity:.96}
.signup-panel h2{font-family:"PT Sans",sans-serif;font-weight:700;font-size:13px}
.signup-panel p{font-size:8px;line-height:8.5px;margin:4px 0 8px}
.field{background:#fff;color:#444;font-family:"PT Sans",sans-serif;font-size:10px;height:24px;border-radius:2px;padding:5px 8px;margin-bottom:4px}
.register{margin-top:8px;width:110px;height:26px;background:var(--blue);font-family:"PT Sans",sans-serif;font-weight:700;font-size:14px;text-align:center;line-height:26px}

/* features */
.features{left:73px;top:350px;width:645px;height:114px;background:var(--soft);display:flex;padding:38px 0 0 32px;gap:30px}
.feature{display:flex;gap:8px;width:180px}
.feature svg{flex:none}
.feature h3{font-family:"Open Sans",sans-serif;font-weight:700;font-size:9.5px;color:var(--blue)}
.feature p{font-size:7.5px;line-height:8px;color:#333;margin-top:2px}

/* chart */
.chart{left:73px;top:500px;width:400px;height:282px;border:1px solid #ccc}
.chart svg{display:block}

/* news */
.news{left:512px;top:494px;width:200px}
.news-head{display:flex;justify-content:space-between;align-items:center}
.news-head h2{font-family:"Open Sans",sans-serif;font-weight:600;font-size:18px;color:#333}
.more-news{background:var(--blue);color:#fff;font-family:Oswald,sans-serif;font-size:8.5px;padding:3px 5px;border-radius:4px}
.item{display:flex;gap:16px;padding:14px 0 6px;border-bottom:1px dotted #777}
.date{width:20px;text-align:center;font-size:7.5px;font-weight:700}
.date b{display:block;width:20px;height:20px;border-radius:50%;background:#333;color:#fff;font-family:Oswald,sans-serif;font-size:10px;line-height:20px;margin-bottom:4px}
.item h4{font-size:8.5px;color:var(--blue);line-height:11px}
.item p{font-size:7.3px;line-height:9.5px;color:#444;margin-top:2px}
.item .more{font-size:6.5px;font-weight:700;margin-top:5px}

/* about */
.divider{left:73px;top:812px;width:645px;height:5px;background:#e0e0e0}
.experts{left:89px;top:846px;font-family:Oswald,sans-serif;font-weight:600;font-size:26px;line-height:28px;color:#333;letter-spacing:-.5px}
.experts .accent{color:var(--blue)}
.experts small{display:block;font-size:9px;line-height:11px;color:#666;margin-top:10px;width:140px;letter-spacing:-.3px}
.about-img{left:262px;top:854px;width:136px;height:88px;border:2px solid #ddd;background:linear-gradient(135deg,#1d3f6a,#6f8fb0 60%,#142a44)}
.welcome{left:414px;top:850px;width:290px}
.welcome h2{font-family:"Open Sans",sans-serif;font-weight:600;font-size:20px;line-height:24px;color:#333}
.welcome h2 span{color:var(--blue);display:block}
.welcome .lead{font-size:11.5px;line-height:14px;color:#777;margin-top:4px}
.body-copy{left:259px;top:954px;width:446px;font-size:8px;line-height:10.5px;color:#333}

/* footer */
.footer{left:0;top:1054px;width:790px;height:146px;background:var(--blue);color:#fff}
.f-brand{left:86px;top:34px;display:flex;align-items:center;gap:8px}
.f-brand .brand-name{color:#fff;font-size:13px}
.f-brand .brand-dot{background:#fff}
.copy{left:86px;top:80px;font-size:6.8px;line-height:8.5px}
.col{top:24px}
.col h5{font-family:"Open Sans",sans-serif;font-weight:600;font-size:13px;margin-bottom:5px}
.col a{display:block;color:#fff;text-decoration:none;font-size:7.5px;line-height:12px}
.socials{display:flex;gap:6px}
.socials i{width:18px;height:18px;border-radius:50%;background:#fff;display:block}
</style>
</head>
<body>

<header>
  <div class="abs brand">
    <div class="brand-name">Veridian Token Bourse</div>
    <div class="brand-dot"></div>
  </div>
  <div class="abs account"><span class="signup">Sign Up</span><span class="login">Log In</span></div>
  <nav class="abs nav"><span class="active">HOME</span>·<span>ABOUT</span>·<span>BUY/SELL</span>·<span>NEWS</span>·<span>CONTACT US</span></nav>
</header>

<div class="abs ticker">
  <div class="tick"><i></i><span>Last Price<br>457.7 USD</span></div>
  <div class="tick"><i></i><span>Low Price<br>449.001 USD</span></div>
  <div class="tick"><i></i><span>High Price<br>471.063 USD</span></div>
  <div class="tick"><i></i><span>Volume<br>346.4 BTC</span></div>
  <div class="tick"><i></i><span>Server Ti<br>23:26:12</span></div>
</div>

<section>
  <div class="abs hero-photo" role="img" aria-label="Businessman in a dark suit holding out his hands, blue toned background"></div>
  <div class="abs coin"></div>
  <div class="abs hero-copy">
    <h1>WHAT IS BITCOIN?</h1>
    <p>BITCOIN IS A DIGITAL CURRENCY YOU CAN USE FOR PERSONAL TRANSACTIONS OR BUSINESS AT HIGH SPEED AND LOW COST.</p>
    <div class="hero-btns"><span>MORE</span><span>HOW TO BUY</span><span>HOW TO SELL</span></div>
  </div>
  <form class="abs signup-panel">
    <h2>Change the world one bitcoin at a time</h2>
    <p>Lorem ipsum dolor sit amet, consectetur adipisicing elit, sed do eiusmod tempor incididunt ut labore et dolore.</p>
    <div class="field">email</div>
    <div class="field">password</div>
    <div class="field">confirm password</div>
    <div class="register">REGISTER</div>
  </form>
</section>

<section class="abs features">
  <div class="feature">
    <svg width="36" height="32" viewBox="0 0 36 32"><circle cx="18" cy="16" r="13" fill="none" stroke="#1a9ad6" stroke-width="3"/><circle cx="13" cy="12" r="3" fill="#1a9ad6"/><circle cx="23" cy="12" r="3" fill="#1a9ad6"/><rect x="10" y="16" width="6" height="10" fill="#1a9ad6"/><rect x="20" y="16" width="6" height="10" fill="#1a9ad6"/></svg>
    <div><h3>LOREM IPSUM DOLOR</h3><p>Duis autem vel eum iriure dolor in hendrerit in vulputate velit esse molestie consequat</p></div>
  </div>
  <div class="feature">
    <svg width="36" height="32" viewBox="0 0 36 32"><circle cx="18" cy="16" r="12" fill="none" stroke="#1a9ad6" stroke-width="5" stroke-dasharray="4 3"/><circle cx="18" cy="16" r="7" fill="#1a9ad6"/></svg>
    <div><h3>UT WISI ENIM AD MINIM</h3><p>Typi non habent claritatem insitam est usus legentis in iis qui facit eorum claritatem. Investigationes</p></div>
  </div>
  <div class="feature">
    <svg width="36" height="32" viewBox="0 0 36 32"><rect x="4" y="6" width="26" height="18" fill="none" stroke="#1a9ad6" stroke-width="2.5"/><path d="M2 27h32M10 10l14 10M24 10L10 20" stroke="#1a9ad6" stroke-width="2.5"/></svg>
    <div><h3>TYPI NON HABENT</h3><p>Nam liber tempor cum soluta nobis eleifend option congue nihil imperdiet doming id quod mazim</p></div>
  </div>
</section>

<section class="abs chart">
  <svg width="400" height="282" viewBox="0 0 400 282" font-family="Arial, sans-serif">
    <defs><linearGradient id="fillArea" x1="0" y1="0" x2="0" y2="1"><stop offset="0" stop-color="#bfe0f4"/><stop offset="1" stop-color="#bfe0f4" stop-opacity="0"/></linearGradient></defs>
    <g font-size="8.5" fill="#333">
      <rect x="10" y="6" width="18" height="12" fill="#fbf5c8" stroke="#aaa" stroke-width=".6"/><text x="13" y="15">M1</text>
      <rect x="28" y="6" width="18" height="12" fill="#fff" stroke="#aaa" stroke-width=".6"/><text x="30" y="15">M5</text>
      <rect x="46" y="6" width="24" height="12" fill="#fff" stroke="#aaa" stroke-width=".6"/><text x="48" y="15">M15</text>
      <rect x="70" y="6" width="24" height="12" fill="#fff" stroke="#aaa" stroke-width=".6"/><text x="72" y="15">M30</text>
      <rect x="94" y="6" width="16" height="12" fill="#fff" stroke="#aaa" stroke-width=".6"/><text x="96" y="15">H1</text>
      <rect x="110" y="6" width="16" height="12" fill="#fff" stroke="#aaa" stroke-width=".6"/><text x="112" y="15">H4</text>
      <text x="181" y="15" font-weight="700" font-size="9">LTC/BTC</text>
    </g>
    <g stroke="#e6e6e6" stroke-width=".7"><line x1="40" y1="66" x2="392" y2="66"/><line x1="40" y1="106" x2="392" y2="106"/><line x1="40" y1="147" x2="392" y2="147"/></g>
    <g font-size="8.5" fill="#333"><text x="9" y="69">0.0253</text><text x="9" y="109">0.0253</text><text x="9" y="150">0.0253</text></g>
    <path d="M41.6 60.8L95.2 60.8L107.2 118.4L112.8 118.4L124.8 176L284.8 176L296.8 146.4L307.2 146.4L319.2 89.6L361.6 89.6L373.6 60.8L391.2 60.8L391.2 180L41.6 180Z" fill="url(#fillArea)"/>
    <polyline points="41.6,60.8 95.2,60.8 107.2,118.4 112.8,118.4 124.8,176 284.8,176 296.8,146.4 307.2,146.4 319.2,89.6 361.6,89.6 373.6,60.8 391.2,60.8" fill="none" stroke="#7fbde6" stroke-width="1.2"/>
    <g font-size="6.5" fill="#444" font-family="Oswald, sans-serif"><text x="72" y="199">22:40</text><text x="131" y="199">22:50</text><text x="190" y="199">23:00</text><text x="249" y="199">23:10</text><text x="309" y="199">23:20</text></g>
    <line x1="102" y1="262" x2="400" y2="262" stroke="#bbb" stroke-dasharray="1.5 1.5"/>
    <g stroke="#ccc"><line x1="101.6" y1="262" x2="101.6" y2="282"/><line x1="200" y1="262" x2="200" y2="282"/><line x1="300" y1="262" x2="300" y2="282"/></g>
    <g font-size="8.5"><text x="33" y="276" fill="#333">QUOTES</text><text x="131" y="277" fill="#999">CANDLES</text><text x="235" y="277" fill="#999">DEPTH</text><text x="331" y="277" fill="#999">VOLUME</text></g>
  </svg>
</section>

<section class="abs news">
  <div class="news-head"><h2>LATEST NEWS</h2><span class="more-news">MORE NEWS</span></div>
  <article class="item"><div class="date"><b>27</b>Mar</div><div><h4>We develop our own softrware APPS and offer business and IT services</h4><p>Lorem ipsum dolor sit amet, consectetur adipisicing elit, sed do eiusmod tempor incididunt ut labore et dolore magna aliqua.</p><div class="more">read more +</div></div></article>
  <article class="item"><div class="date"><b>12</b>Feb</div><div><h4>We develop our own softrware APPS and offer business and IT services</h4><p>Lorem ipsum dolor sit amet, consectetur adipisicing elit, sed do eiusmod tempor incididunt ut labore et dolore magna aliqua.</p><div class="more">read more +</div></div></article>
  <article class="item"><div class="date"><b>12</b>Feb</div><div><h4>We develop our own softrware APPS and offer business and IT services</h4><p>Lorem ipsum dolor sit amet, consectetur adipisicing elit, sed do eiusmod tempor incididunt ut labore et dolore magna aliqua.</p><div class="more">read more +</div></div></article>
</section>

<div class="abs divider"></div>

<section>
  <div class="abs experts">WE ARE<br>EXPERTS IN<br><span class="accent">BITCOIN</span><br>TECHONOGIES
    <small>LOREM IPSUM DOLOR SIT AMET, CONSECTETUR ADIPISICING ELIT, SED DO EIUSMOD TEMPOR.</small>
  </div>
  <div class="abs about-img" role="img" aria-label="Coin stacks with a coin stamped BIT over a blue digital world map"></div>
  <div class="abs welcome">
    <h2>WELCOME TO<span>VERIDIAN TOKEN BOURSE</span></h2>
    <p class="lead">Lorem ipsum dolor sit amet, consectetur a dipisicing elit, sed do eiusmod tempor &nbsp;incididunt ut labore et dolore.</p>
  </div>
  <p class="abs body-copy">At vero eos et accusamus et iusto odio dignissimos ducimus, qui blanditiis praesentium voluptatum deleniti atque corrupti, quos dolores et quas molestias excepturi sint, obcaecati cupiditate non provident, similique sunt in culpa, qui officia deserunt mollitia animi, id est laborum et dolorum fuga. Et harum quidem rerum facilis est et expedita distinctio. Nam libero tempore, cum soluta nobis est eligendi optio, cumque nihil impeit, quo minus id, quod maxime placeat, facere possimus, omnis voluptas assumenda est, om</p>
</section>

<footer class="abs footer">
  <div class="abs f-brand"><div class="brand-name">Veridian Token Bourse</div><div class="brand-dot"></div></div>
  <div class="abs copy">© 2014 Veridian Token Bourse.<br>All rights reserved</div>
  <div class="abs col" style="left:267px"><h5>ABOUT</h5><a>About us</a><a>Who we are</a><a>Why we are different</a><a>Terms of Use</a><a>Privacy Policy</a><a>Cookies Statement</a></div>
  <div class="abs col" style="left:386px"><h5>HELP</h5><a>What is Bitcoin?</a><a>How to buy Bitcoins?</a><a>How to sell Bitcoins?</a><a>FAQ</a></div>
  <div class="abs col" style="left:500px"><h5>DATA</h5><a>What is Bitcoin?</a><a>How to buy Bitcoins?</a><a>How to sell Bitcoins?</a><a>FAQ</a></div>
  <div class="abs col" style="left:619px"><h5>FOLLOW VTB</h5><div class="socials"><i></i><i></i><i></i></div></div>
</footer>

</body>
</html>
```